Free T-Shirt banner

I am a small auto parts store and I would like a banner 30" tall by 72" wide. It is to be very eye catching and have "Free T-Shirt" and "with $100 purchase" written on it. I took some pictures of our t-shirts, let me know if you need them positioned differently

```html
<!DOCTYPE html>
<html lang="en">
<head>
<meta charset="UTF-8">
<title>Free T-Shirt Banner</title>
<link href="https://fonts.googleapis.com/css2?family=Oswald:wght@600&family=Yellowtail&family=Roboto:wght@700&display=swap" rel="stylesheet">
<style>
  :root {
    --canvas-grey: #7b7b7b;
    --panel-black: #1b1b1b;
    --panel-black-edge: #262626;
    --promo-yellow: #f6d811;
    --promo-yellow-deep: #e9c400;
    --text-white: #ffffff;
    --shirt-red: #e8204a;
    --shirt-grey: #55524f;
    --shirt-black: #141414;
  }
  * { margin: 0; padding: 0; box-sizing: border-box; }
  html, body {
    width: 1200px;
    height: 1061px;
    overflow: hidden;
    background: var(--canvas-grey);
  }
  .canvas {
    position: relative;
    width: 1200px;
    height: 1061px;
  }
  .banner {
    position: absolute;
    left: 141px;
    width: 933px;
    overflow: hidden;
    background: radial-gradient(circle at 75% 50%, var(--promo-yellow) 0%, var(--promo-yellow) 55%, var(--promo-yellow-deep) 100%);
  }
  .banner--white-script { top: 99px; height: 348px; }
  .banner--yellow-script { top: 522px; height: 384px; }
  .banner__dark-panel {
    position: absolute;
    inset: 0;
    width: 100%;
    height: 100%;
  }
  .banner__copy {
    position: absolute;
    left: 63px;
    top: 58px;
    color: var(--text-white);
  }
  .banner--yellow-script .banner__copy { top: 66px; }
  .headline {
    font-family: 'Oswald', 'Arial Narrow', sans-serif;
    font-weight: 600;
    font-size: 138px;
    line-height: 1;
    letter-spacing: 1px;
  }
  .script-line {
    font-family: 'Yellowtail', cursive;
    font-size: 84px;
    line-height: 1;
    margin-top: -2px;
    margin-left: 2px;
  }
  .banner--yellow-script .script-line { color: var(--promo-yellow); }
  .offer {
    font-family: 'Roboto', Arial, sans-serif;
    font-weight: 700;
    font-size: 19px;
    letter-spacing: 0.6px;
    margin-top: 14px;
    margin-left: 4px;
  }
  .shirt-photo {
    position: absolute;
    right: 58px;
    top: 20px;
    width: 430px;
    height: 300px;
    border-radius: 8px;
    background: linear-gradient(100deg, var(--shirt-black) 0%, var(--shirt-grey) 30%, var(--shirt-red) 42%, var(--shirt-red) 100%);
    box-shadow: 0 10px 22px rgba(0,0,0,0.35);
  }
  .banner--yellow-script .shirt-photo { top: 30px; height: 320px; }
</style>
</head>
<body>
<main class="canvas">

  <section class="banner banner--white-script">
    <svg class="banner__dark-panel" viewBox="0 0 933 348" preserveAspectRatio="none" aria-hidden="true">
      <polygon points="0,0 475,0 345,348 0,348" fill="var(--panel-black)"/>
      <polygon points="460,0 475,0 345,348 330,348" fill="var(--panel-black-edge)"/>
    </svg>
    <div class="banner__copy">
      <div class="headline">FREE</div>
      <div class="script-line">T-Shirt</div>
      <div class="offer">WITH $100 PURCHASE</div>
    </div>
    <div class="shirt-photo" role="img" aria-label="Photo of three stacked store t-shirts in black, grey and red with printed graphics"></div>
  </section>

  <section class="banner banner--yellow-script">
    <svg class="banner__dark-panel" viewBox="0 0 933 384" preserveAspectRatio="none" aria-hidden="true">
      <polygon points="0,0 475,0 345,384 0,384" fill="var(--panel-black)"/>
      <polygon points="460,0 475,0 345,384 330,384" fill="var(--panel-black-edge)"/>
    </svg>
    <div class="banner__copy">
      <div class="headline">FREE</div>
      <div class="script-line">T-Shirt</div>
      <div class="offer">WITH $100 PURCHASE</div>
    </div>
    <div class="shirt-photo" role="img" aria-label="Photo of three stacked store t-shirts in black, grey and red with printed graphics"></div>
  </section>

</main>
</body>
</html>
```